Varnel Group Limited Stationary

We are in need of business card and letterhead designs. We are looking for clean modern designs that complement the style and feel of our logo.

Industry/Entity Type

Business

```html
<!DOCTYPE html>
<html lang="en">
<head>
<meta charset="utf-8">
<title>Varnel Group Limited Stationery</title>
<link href="https://fonts.googleapis.com/css2?family=EB+Garamond:wght@400;500&family=Open+Sans:wght@400;600&family=Great+Vibes&display=swap" rel="stylesheet">
<style>
  :root {
    --brand-blue: #0b3d86;
    --paper: #ffffff;
    --backdrop: #ececec;
    --ink: #4a4a4a;
    --ink-soft: #7a7a7a;
    --watermark: #eeeeee;
  }
  * { box-sizing: border-box; margin: 0; padding: 0; }
  html, body { width: 1200px; height: 795px; overflow: hidden; }
  body { background: var(--backdrop); position: relative; font-family: "Open Sans", sans-serif; color: var(--ink); }

  .brand-name {
    font-family: "EB Garamond", serif;
    font-weight: 500;
    color: var(--brand-blue);
    text-transform: uppercase;
    letter-spacing: 1px;
    white-space: nowrap;
  }
  .brand { display: flex; align-items: center; gap: 8px; }
  .brand-dot { border-radius: 50%; background: var(--brand-blue); flex: none; }

  /* Letterhead */
  .letterhead {
    position: absolute; left: 650px; top: 86px; width: 440px; height: 622px;
    background: var(--paper); overflow: hidden;
    box-shadow: 0 2px 10px rgba(0,0,0,.12);
  }
  .letterhead .brand { position: absolute; left: 40px; top: 36px; padding-bottom: 5px; border-bottom: 1px solid var(--brand-blue); }
  .letterhead .brand-name { font-size: 17px; }
  .letterhead .brand-dot { width: 16px; height: 16px; }
  .letterhead-contact {
    position: absolute; right: 36px; top: 96px; font-family: "EB Garamond", serif;
    font-size: 7px; line-height: 10px; color: var(--ink-soft);
  }
  .letterhead-contact b { color: var(--brand-blue); font-weight: 500; }
  .letter-body { position: absolute; left: 40px; top: 110px; width: 300px; font-size: 7.5px; line-height: 11px; }
  .letter-body p { margin-bottom: 9px; }
  .letter-salutation { font-weight: 600; }
  .signature { position: absolute; left: 40px; top: 390px; }
  .signature-script { font-family: "Great Vibes", cursive; font-size: 28px; color: #555; line-height: 1; }
  .signature-role { font-size: 8px; font-weight: 600; color: #555; }
  .letterhead-watermark {
    position: absolute; right: 30px; bottom: 30px; width: 200px; height: 200px;
    border-radius: 50%; border: 26px solid var(--watermark);
  }
  .letterhead-band { position: absolute; left: 0; right: 0; bottom: 0; height: 8px; background: var(--brand-blue); }

  /* Business cards */
  .card {
    position: absolute; width: 336px; height: 192px; overflow: hidden;
    box-shadow: 0 2px 8px rgba(0,0,0,.14);
  }
  .card-back { left: 160px; top: 150px; background: var(--brand-blue); }
  .card-back .brand { position: absolute; left: 50%; top: 50%; transform: translate(-50%, -50%); }
  .card-back .brand-dot { width: 26px; height: 26px; background: #fff; }
  .card-back .brand-name { color: #fff; font-size: 20px; }
  .card-back-web {
    position: absolute; left: 14px; bottom: 14px; font-family: "EB Garamond", serif;
    font-size: 8px; color: #fff;
  }

  .card-front { left: 160px; top: 430px; background: var(--paper); }
  .card-front .brand { position: absolute; left: 22px; top: 26px; padding-bottom: 4px; border-bottom: 1px solid var(--brand-blue); }
  .card-front .brand-name { font-size: 16px; }
  .card-front .brand-dot { width: 15px; height: 15px; }
  .card-person { position: absolute; left: 190px; top: 62px; font-family: "EB Garamond", serif; color: var(--ink); }
  .card-person-name { font-size: 13px; }
  .card-person-role { font-size: 7px; letter-spacing: 1.5px; text-transform: uppercase; margin-bottom: 8px; }
  .card-contact { font-size: 8px; line-height: 11px; }
  .card-contact b { color: var(--brand-blue); font-weight: 500; display: inline-block; width: 9px; }
  .card-address { font-size: 8px; line-height: 11px; margin-top: 6px; }
  .card-band { position: absolute; left: 0; right: 0; bottom: 0; height: 7px; background: var(--brand-blue); }
</style>
</head>
<body>

<section class="letterhead">
  <div class="brand">
    <span class="brand-name">Varnel Group</span>
    <span class="brand-dot"></span>
  </div>

  <address class="letterhead-contact">
    <b>T</b> (555) 014 2287<br>
    <b>F</b> (555) 014 2290<br>
    <b>E</b> info@varnelgroup.com<br>
    48 Harbor Street, #210<br>
    Springfield IL 62701<br>
    www.varnelgroup.com
  </address>

  <div class="letter-body">
    <p class="letter-salutation">Lorem ipsum,</p>
    <p>Cras mattis consectetur purus sit amet fermentum. Etiam porta sem malesuada magna mollis euismod. Integer posuere erat a ante venenatis dapibus posuere velit aliquet. Cras justo odio, dapibus ac facilisis in, egestas eget quam.</p>
    <p>Vivamus sagittis lacus vel augue laoreet rutrum faucibus dolor auctor. Donec sed odio dui. Etiam porta sem malesuada magna mollis euismod.</p>
    <p>Donec id elit non mi porta gravida at eget metus. Fusce dapibus, tellus ac cursus commodo, tortor mauris condimentum nibh, ut fermentum massa justo sit amet risus.</p>
    <p>Cum sociis natoque penatibus et magnis dis parturient montes, nascetur ridiculus mus. Curabitur blandit tempus porttitor.</p>
    <p>Nullam quis risus eget urna mollis ornare vel eu leo. Aenean lacinia bibendum nulla sed consectetur.</p>
  </div>

  <div class="signature">
    <div class="signature-script">Your Name</div>
    <div class="signature-role">Company Director</div>
  </div>

  <div class="letterhead-watermark"></div>
  <div class="letterhead-band"></div>
</section>

<section class="card card-back">
  <div class="brand">
    <span class="brand-dot"></span>
    <span class="brand-name">Varnel Group</span>
  </div>
  <div class="card-back-web">www.varnelgroup.com</div>
</section>

<section class="card card-front">
  <div class="brand">
    <span class="brand-name">Varnel Group</span>
    <span class="brand-dot"></span>
  </div>
  <div class="card-person">
    <div class="card-person-name">Elena Marsh</div>
    <div class="card-person-role">Manager</div>
    <div class="card-contact">
      <b>T</b> (555) 014 2287<br>
      <b>F</b> (555) 014 2290<br>
      <b>E</b> emarsh@varnelgroup.com
    </div>
    <div class="card-address">48 Harbor Street, #210<br>Springfield IL 62701</div>
  </div>
  <div class="card-band"></div>
</section>

</body>
</html>
```